Birchwell Craft House business card design- Fine Art sculpture business (Contract guaranteed)

This business card is for a fine art business. Though we don't have a website up and running yet it should be up soon. I would like the business card to be elegant and fairly simple with a picture of one of my sculptures on the front (you might need to photoshop out the background) as well as my basic contact info (my name,phone # and e-mail). On the back I'd like it to be pretty simple with just "Notes" and some blank lines for writing in info.
Updates

Target Market(s)

High end artwork buyers

Industry/Entity Type

Art Gallery

Contact Information for Business Card

Wendell Marsh Phone: (555) 312-4098 E-mail: wendell@quarrymint.example Facebook: @birchwellcrafthouse Instagram: birchwellcrafthouse

Colors

Designer to choose colors to be used in the design.

Requirements
Must have
• *A picture of one of my sculptures*, my name, business name (Birchwell Craft House), e-mail, phone #, and a notes section on the back.
• Birchwell Craft House
• Wendell Marsh
• (555)312-4098
• wendell@quarrymint.example
• Facebook: @birchwellcrafthouse
• Instagram: birchwellcrafthouse
Nice to have
• It'd be nice if you can crop out the background in the sculpture pictures, which ever one you end up using.

```html
<!DOCTYPE html>
<html lang="en">
<head>
<meta charset="utf-8">
<title>Birchwell Craft House — Business Card</title>
<link rel="stylesheet" href="https://fonts.googleapis.com/css2?family=EB+Garamond:wght@400;500&display=swap">
<style>
  :root {
    --backdrop: #3d3d3d;
    --card: #f4f4f4;
    --card-edge: #e2e2e2;
    --ink: #4a4a4a;
    --ink-soft: #6a6a6a;
    --rule: #9a9a9a;
    --amethyst-deep: #4a2c80;
    --amethyst: #8a5cc8;
    --amethyst-pale: #d9cdea;
  }
  * { box-sizing: border-box; margin: 0; padding: 0; }
  html, body { width: 1200px; height: 1000px; overflow: hidden; }
  body {
    background: var(--backdrop);
    font-family: "EB Garamond", Garamond, serif;
    color: var(--ink);
    display: flex;
    flex-direction: column;
    align-items: center;
    justify-content: center;
    gap: 56px;
  }
  .card {
    position: relative;
    width: 700px;
    height: 400px;
    background: var(--card);
    border: 1px solid var(--card-edge);
    overflow: hidden;
  }

  /* Back: notes side */
  .notes-title {
    position: absolute;
    top: 40px;
    left: 0;
    right: 0;
    text-align: center;
    font-size: 22px;
    font-weight: 400;
    letter-spacing: 0.14em;
    color: var(--ink);
  }
  .notes-lines {
    position: absolute;
    top: 100px;
    left: 70px;
    right: 70px;
  }
  .notes-line {
    height: 44px;
    border-bottom: 1.5px dotted var(--rule);
  }
  .notes-line.short { margin-left: 45%; }
  .notes-sculpture {
    position: absolute;
    left: 0;
    bottom: 0;
    width: 300px;
    height: 90px;
    background: linear-gradient(135deg, var(--amethyst) 0%, var(--amethyst-deep) 100%);
  }

  /* Front: contact side */
  .front-sculpture {
    position: absolute;
    left: 60px;
    right: 0;
    top: 40px;
    height: 190px;
    background: linear-gradient(110deg, var(--amethyst-pale) 0%, var(--amethyst) 45%, var(--amethyst-deep) 100%);
  }
  .business-name {
    position: absolute;
    top: 244px;
    right: 60px;
    font-size: 30px;
    font-weight: 400;
    letter-spacing: 0.12em;
    text-transform: uppercase;
    color: var(--ink);
  }
  .contact-line {
    position: absolute;
    left: 0;
    right: 0;
    bottom: 46px;
    display: flex;
    justify-content: center;
    align-items: center;
    gap: 12px;
    font-size: 20px;
    color: var(--ink-soft);
  }
  .contact-item { display: flex; align-items: center; gap: 8px; }
  .contact-sep { color: var(--ink-soft); }
  .contact-icon { width: 20px; height: 20px; flex: none; }
</style>
</head>
<body>

  <section class="card card-back" aria-label="Card back">
    <h2 class="notes-title">NOTES</h2>
    <div class="notes-lines">
      <div class="notes-line"></div>
      <div class="notes-line"></div>
      <div class="notes-line"></div>
      <div class="notes-line"></div>
      <div class="notes-line short"></div>
    </div>
    <div class="notes-sculpture" role="img" aria-label="Photograph of the artist's crystal sculpture, cropped at the card edge"></div>
  </section>

  <section class="card card-front" aria-label="Card front">
    <div class="front-sculpture" role="img" aria-label="Photograph of the artist's arching crystal sculpture"></div>

    <h1 class="business-name">Birchwell Craft House</h1>

    <div class="contact-line">
      <span class="contact-item contact-name">Wendell Marsh</span>
      <span class="contact-sep">|</span>
      <span class="contact-item contact-phone">
        <svg class="contact-icon" viewBox="0 0 20 20" aria-hidden="true">
          <circle cx="10" cy="10" r="10" fill="var(--ink)"/>
          <path d="M7 5.5 L8.6 5.5 L9.2 8 L8.2 9 Q9 11 11 11.8 L12 10.8 L14.5 11.4 L14.5 13 Q14.5 14.5 13 14.5 Q5.5 14 5.5 7 Q5.5 5.5 7 5.5 Z" fill="var(--card)"/>
        </svg>
        (555) 312-4098
      </span>
      <span class="contact-sep">|</span>
      <span class="contact-item contact-email">
        <svg class="contact-icon" viewBox="0 0 20 20" aria-hidden="true">
          <circle cx="10" cy="10" r="10" fill="var(--ink)"/>
          <rect x="5" y="6.5" width="10" height="7" fill="var(--card)"/>
          <path d="M5 6.5 L10 10.5 L15 6.5" fill="none" stroke="var(--ink)" stroke-width="1"/>
        </svg>
        wendell@quarrymint.example
      </span>
    </div>
  </section>

</body>
</html>
```